Fernbrook Pet Showcase Ticket Card Design

We’re looking to create a complimentary “ticket” card for Fernbrook Pet Showcase that can be handed out physically. We host an event for cat lovers. The card should feel special and collectible. Size will be a standard business card (3.5" x 2") Orientation is open to designer recommendation. This ticket will be used as a complimentary entry pass for select guests, partners, & giveaways. Key elements to Include are the Fernbrook Pet Showcase logo (provided), the words “Complimentary Ticket” or similar wording (open to creative phrasing and cat puns) A blank space for the Event date (to be written in) & Ticket number (to be written in) . Event Name is always "Fernbrook Pet Bazaar & Rehoming Day". We want the ticket to feel clean & modern but slightly playful with a cat-inspired touch (think clever, not kitschy). Could include a subtle cat motif or texture (e.g., whisker lines, paw detail, soft patterning) Open to unique layout ideas that still leave clear writing space. Avoid overcrowding of elements. Ticket should also have fine print "This ticket is not redeemable for cash and cannot be combined with any other offers or discounts, can only be used for the date indicated"

Target Market(s)

Women

Industry/Entity Type

pets

Colors
6B429C
8869AF
B7A5CE
E3DAEB
F3F0F8

Requirements
Must have
• Fernbrook Pet Showcase Logo & words around complimentary ticket as well as the fine print
Nice to have
• cat-inspired touch (think clever, not kitschy). Could include a subtle cat motif or texture (e.g., whisker lines, paw detail, soft patterning)
Should not have
• should not look cartoony

```html
<!DOCTYPE html>
<html lang="en">
<head>
<meta charset="utf-8">
<title>Fernbrook Pet Showcase – Complimentary Ticket</title>
<link href="https://fonts.googleapis.com/css2?family=Urbanist:wght@400;500;700;800&display=swap" rel="stylesheet">
<style>
  :root {
    --violet-deep: #6B429C;
    --violet: #8869AF;
    --lilac: #B7A5CE;
    --lilac-pale: #E3DAEB;
    --mist: #F3F0F8;
    --ink: #1d1b20;
    --panel: #28252b;
    --paper: #ffffff;
    --backdrop: #eeeef0;
    --gold: #f2d36b;
    --amber: #d98a2b;
  }
  * { margin: 0; padding: 0; box-sizing: border-box; }
  html, body {
    width: 976px; height: 1200px; overflow: hidden;
    background: var(--backdrop);
    font-family: "Urbanist", sans-serif;
  }
  .ticket {
    position: absolute; left: 100px; top: 378px;
    width: 777px; height: 444px;
    background: var(--paper);
    box-shadow: 0 24px 40px rgba(0,0,0,0.18);
    overflow: hidden;
  }
  .ticket-curves { position: absolute; inset: 0; }
  .event-band {
    position: absolute; left: 41px; top: 48px;
    width: 334px; height: 48px;
    background: var(--violet);
    transform: rotate(-2.6deg);
    transform-origin: left top;
    box-shadow: 0 8px 14px rgba(60,40,90,0.18);
    display: flex; align-items: center; justify-content: center;
  }
  .event-band-text {
    color: var(--paper); font-weight: 800; font-size: 34px;
    letter-spacing: -0.5px; line-height: 1; margin-top: 4px;
  }
  .event-title {
    position: absolute; left: 76px; top: 124px;
    color: var(--ink); font-weight: 800; font-size: 55px;
    line-height: 60px; letter-spacing: -1px;
  }
  .write-in {
    position: absolute; top: 279px; height: 117px;
    border: 1.2px dashed var(--ink);
  }
  .write-in-date { left: 39px; width: 291px; }
  .write-in-number { left: 343px; width: 109px; }
  .paw-mark {
    position: absolute; width: 54px; height: 54px;
    border-radius: 50% 50% 46% 46%;
    background: var(--violet-deep);
  }
  .paw-mark-one { left: 368px; top: 48px; transform: rotate(12deg); }
  .paw-mark-two { left: 428px; top: 94px; transform: rotate(-8deg); }
  .heart-mark { position: absolute; border-radius: 50%; background: var(--gold); }
  .heart-a { left: 67px; top: 42px; width: 18px; height: 18px; }
  .heart-b { left: 488px; top: 190px; width: 13px; height: 13px; background: var(--amber); }
  .heart-c { left: 226px; top: 253px; width: 11px; height: 11px; }
  .heart-d { left: 48px; top: 266px; width: 20px; height: 20px; }

  .pass-panel {
    position: absolute; left: 537px; top: 0;
    width: 240px; height: 444px;
    background: var(--panel);
    color: var(--paper);
    text-align: center;
  }
  .brand-name {
    position: absolute; left: 0; right: 0; top: 104px;
    font-weight: 800; font-size: 29px; line-height: 31px;
    letter-spacing: -0.3px;
  }
  .pass-label {
    position: absolute; left: 0; right: 0; top: 220px;
    font-weight: 500; font-size: 20px; line-height: 24px;
  }
  .fine-print {
    position: absolute; left: 42px; right: 42px; top: 292px;
    font-weight: 500; font-size: 11px; line-height: 13.8px;
    letter-spacing: -0.2px;
  }
</style>
</head>
<body>
  <main class="ticket">
    <svg class="ticket-curves" width="777" height="444" viewBox="0 0 777 444" aria-hidden="true">
      <path d="M0 44 C40 20 110 10 160 56" fill="none" stroke="var(--lilac)" stroke-width="1.5"/>
      <path d="M294 46 L320 0" fill="none" stroke="var(--lilac)" stroke-width="1.5"/>
      <path d="M458 444 C452 400 490 380 537 366" fill="none" stroke="var(--lilac)" stroke-width="1.5"/>
    </svg>

    <div class="event-band"><span class="event-band-text">Fernbrook Pet</span></div>
    <h1 class="event-title">Bazaar &amp;<br>Rehoming Day.</h1>

    <div class="paw-mark paw-mark-one" role="img" aria-label="Purple paw print"></div>
    <div class="paw-mark paw-mark-two" role="img" aria-label="Purple paw print"></div>
    <div class="heart-mark heart-a" role="img" aria-label="Small gold heart"></div>
    <div class="heart-mark heart-b" role="img" aria-label="Small amber heart"></div>
    <div class="heart-mark heart-c" role="img" aria-label="Small gold heart"></div>
    <div class="heart-mark heart-d" role="img" aria-label="Small gold heart"></div>

    <div class="write-in write-in-date" aria-label="Event date"></div>
    <div class="write-in write-in-number" aria-label="Ticket number"></div>

    <aside class="pass-panel">
      <p class="brand-name">Fernbrook<br>Pet Showcase</p>
      <p class="pass-label">Complimentary<br>Ticket</p>
      <p class="fine-print">This ticket is not redeemable for cash and cannot be combined with other offers or discounts. Valid only for the date indicated.</p>
    </aside>
  </main>
</body>
</html>
```